Professional Home Buyer business card needed

I need a pretty straight forward business card designed. We help people that NEED to sell their homes solve problems. We perform all types of Real Estate transactions including flip, wholesale, investment, rental property and multi family. The card will mainly be used to give to prospective Sellers but will also be given to Real Estate Investors as well. It should professional and very easy to read, most clients are older people.

Target Market(s)

Distressed home sellers as well as Real Estate investors

Industry/Entity Type

Real Estate

Contact Information for Business Card

should be a professional layout

Colors
ec1f27
ffffff
000000

Requirements
Must have
• Large logo on back and smaller one on front. should utilize Red, white, and black.
• I am thinking of using a soft touch coating on the card so keep that in mind.
• Contact info should be very easy to read, think older clients.
Nice to have
• I would like to see a design with rounded corners on the card
Should not have
• pictures of homes or other home graphics.

```html
<!DOCTYPE html>
<html lang="en">
<head>
<meta charset="utf-8">
<title>Summit Home Buyers – Business Card</title>
<link rel="stylesheet" href="https://fonts.googleapis.com/css2?family=Saira:wght@700&family=Montserrat:wght@300;600&display=swap">
<style>
  :root {
    --brand-red: #ec1f27;
    --brand-black: #0b0b0c;
    --brand-white: #ffffff;
    --canvas-bg: #ffffff;
    --shadow: rgba(0, 0, 0, 0.35);
  }
  * { margin: 0; padding: 0; box-sizing: border-box; }
  html, body {
    width: 1200px; height: 1000px; overflow: hidden;
    background: var(--canvas-bg);
  }
  .canvas { position: relative; width: 1200px; height: 1000px; }

  .card {
    position: absolute; left: 234px; width: 732px; height: 417px;
    overflow: hidden;
    box-shadow: 6px 7px 8px var(--shadow);
  }
  .card--front { top: 54px; background: var(--brand-white); }
  .card--back { top: 528px; background: var(--brand-black); }

  .card__waves { position: absolute; inset: 0; width: 732px; height: 417px; }

  .brand {
    position: absolute; left: 0; width: 100%;
    display: flex; align-items: center; justify-content: center;
    font-family: "Saira", sans-serif; font-weight: 700;
    line-height: 1; letter-spacing: 0.04em; white-space: nowrap;
  }
  .brand__mark { flex: none; background: var(--brand-red); }

  .card--front .brand { top: 108px; font-size: 42px; color: var(--brand-black); }
  .card--front .brand__mark { width: 22px; height: 22px; margin-right: 16px; }

  .card--back .brand { top: 178px; font-size: 50px; color: var(--brand-white); }
  .card--back .brand__mark { width: 26px; height: 26px; margin-right: 18px; }

  .person {
    position: absolute; right: 401px; top: 308px; text-align: right;
    font-family: "Montserrat", sans-serif; color: var(--brand-white);
  }
  .person__name { font-size: 28px; font-weight: 600; line-height: 1.1; }
  .person__name-accent { color: var(--brand-red); }
  .person__title { font-size: 21px; font-weight: 300; line-height: 1.2; }

  .divider {
    position: absolute; left: 365px; top: 286px; width: 3px; height: 101px;
    background: var(--brand-white);
  }

  .contact {
    position: absolute; left: 394px; top: 295px; list-style: none;
    font-family: "Montserrat", sans-serif; font-weight: 300;
    font-size: 20px; color: var(--brand-white);
  }
  .contact__item { display: flex; align-items: center; height: 27px; }
  .contact__icon { width: 22px; height: 20px; margin-right: 14px; flex: none; }
  .contact__icon .icon-fill { fill: var(--brand-red); }
  .contact__icon .icon-cut { fill: var(--brand-black); }
</style>
</head>
<body>
<main class="canvas">

  <section class="card card--front" aria-label="Business card front">
    <svg class="card__waves" viewBox="0 0 732 417" aria-hidden="true">
      <path d="M0,226 Q300,292 732,214 L732,417 L0,417 Z" fill="var(--brand-black)"/>
      <path d="M0,194 Q250,238 526,236 Q250,252 0,212 Z" fill="var(--brand-black)"/>
      <path d="M732,192 Q500,258 200,262 Q500,254 732,206 Z" fill="var(--brand-red)"/>
    </svg>

    <h1 class="brand"><span class="brand__mark"></span>SUMMIT HOME BUYERS</h1>

    <div class="person">
      <p class="person__name">Your <span class="person__name-accent">Name</span></p>
      <p class="person__title">Your Title</p>
    </div>

    <div class="divider"></div>

    <ul class="contact">
      <li class="contact__item">
        <svg class="contact__icon" viewBox="0 0 24 24" aria-hidden="true"><path class="icon-fill" d="M6.6 10.8c1.4 2.8 3.8 5.1 6.6 6.6l2.2-2.2c.3-.3.7-.4 1-.2 1.1.4 2.3.6 3.6.6.6 0 1 .4 1 1V20c0 .6-.4 1-1 1C10.6 21 3 13.4 3 4c0-.6.4-1 1-1h3.5c.6 0 1 .4 1 1 0 1.3.2 2.5.6 3.6.1.3 0 .7-.2 1z"/></svg>
        123-456-2100
      </li>
      <li class="contact__item">
        <svg class="contact__icon" viewBox="0 0 24 24" aria-hidden="true"><path class="icon-fill" d="M2 5h20v2l-10 6L2 7z"/><path class="icon-fill" d="M2 9l10 6 10-6v10H2z"/></svg>
        youremail@example.com
      </li>
      <li class="contact__item">
        <svg class="contact__icon" viewBox="0 0 24 24" aria-hidden="true"><circle class="icon-fill" cx="12" cy="12" r="10"/><path class="icon-cut" d="M12 6l2 3.5-2 2.5-2-2.5zM6 13l3.5-1 1.5 2.5-2.5 2.5zM18 13l-3.5-1-1.5 2.5 2.5 2.5z"/></svg>
        www.yourwebsite.com
      </li>
    </ul>
  </section>

  <section class="card card--back" aria-label="Business card back">
    <h2 class="brand"><span class="brand__mark"></span>SUMMIT HOME BUYERS</h2>
  </section>

</main>
</body>
</html>
```